Torvane Center for Restorative Medicine

I need a full informational website for my medical practice. I would like to use my logo and also include a lot of emblems/pictures (also a picture of me in a white coat). The website should have a function for people to inquire and send me messages. I will be offering needle-less regenerative injection therapy, stem cell treatments, bioidentical hormone therapy, treatment for chronic illness, neurodegenerative diseases, skin rejuvenation, hair restoration, male enhancement, female enhancement, and anti-aging. The practice will not be accepting insurance and will be cash/credit card only.
A good example of written content and functionality is this website:
http://thebqvx.example/. However, I want different theme and tones.
Target Market(s)
High end clientele in Los Angeles, Southern California. Health minded people who are interested in living better and longer and can afford anti-aging treatments. Men and women who want to improve sexual health and wellbeing.
Industry/Entity Type
Medical And Science
Coding
Coded - Design and coding required
Number of Pages Required
5+ page
Font styles to use
Requirements
Must have
- 1. I will need to be able to move the site to other servers (needed for site speed)
- 2. Site must be build on WordPress
- 3. Full admin credentials for domain, cpanel, wordpress, ftp.
- 4. No third party interaction on development and content deployment once the site is on different servers
- 5. I will need the ability to add content and links to the site
- 6. I will need the ability to optimize the site for speed
- 7. I will need to ability to modify URLs so they are more SEO friendly
Nice to have
- pictures of stem cells, health improvement and regeneration, beauty, youthful individuals, older healthy and happy individuals. Medical designs.
Should not have
- flowers, dna

```html
<!DOCTYPE html>
<html lang="en">
<head>
<meta charset="utf-8">
<title>Torvane Center for Restorative Medicine</title>
<link rel="stylesheet" href="https://fonts.googleapis.com/css2?family=Poppins:wght@400;500;600;700&family=Open+Sans:wght@400;600;700&display=swap">
<style>
:root{
  --green:#1fa87a;
  --green-btn:#3aa948;
  --teal-dark:#0d5b69;
  --teal-deep:#0a4c58;
  --ink:#1d1d1d;
  --body:#444;
  --muted:#666;
  --pale:#eef6f8;
  --map:#e6eaec;
  --white:#fff;
}
*{box-sizing:border-box;margin:0;padding:0}
html,body{width:1200px;height:2773px;overflow:hidden}
body{position:relative;font-family:"Open Sans",Arial,sans-serif;color:var(--body);background:var(--white);font-size:11px;line-height:1.6}
.abs{position:absolute}
h1,h2,h3,h4{font-family:"Poppins",Arial,sans-serif;color:var(--ink)}
.btn{position:absolute;display:flex;align-items:center;justify-content:center;border-radius:20px;font-family:"Poppins",sans-serif;font-size:9px;font-weight:600;letter-spacing:.5px;text-transform:uppercase}
.btn-solid{background:var(--green-btn);color:var(--white)}
.btn-line{border:1.5px solid #8cd49a;color:var(--green-btn);text-transform:none;font-weight:500;font-size:10px;background:var(--white)}

/* header */
.topbar{top:0;left:0;width:1200px;height:62px;background:var(--white)}
.brand{left:244px;top:14px;display:flex;align-items:center;gap:8px}
.brand-dot{width:30px;height:30px;border-radius:50%;background:var(--teal-dark)}
.brand-name{font-family:"Poppins",sans-serif;font-weight:600;font-size:22px;color:var(--teal-dark);letter-spacing:2px}
.help{left:497px;top:14px;font-size:10px;color:var(--ink)}
.help strong{display:block;color:var(--green);font-family:"Poppins",sans-serif;font-size:14px;font-weight:600;line-height:1.3}
.info{display:flex;gap:8px;font-size:9px;color:var(--body);line-height:1.55;top:14px;white-space:nowrap}
.info .ico{width:18px;height:18px;border-radius:50%;background:var(--green);flex:none;display:flex;align-items:center;justify-content:center}
.vline{top:12px;width:1px;height:36px;background:#ddd}
.nav{top:62px;left:0;width:1200px;height:30px;background:var(--green)}
.nav ul{position:absolute;left:244px;top:0;display:flex;gap:22px;list-style:none;height:30px;align-items:center}
.nav li{font-family:"Poppins",sans-serif;font-size:8.5px;font-weight:600;color:var(--white);text-transform:uppercase}
.nav li.active{border-bottom:2px solid var(--white);padding-bottom:2px}
.nav-tools{right:245px;top:8px;display:flex;gap:14px}

/* hero */
.hero{top:92px;left:0;width:1200px;height:386px;background:radial-gradient(ellipse at 25% 50%,#5fae7b 0%,#3f9668 45%,#2f8560 100%)}
.hero-photo{top:92px;left:610px;width:590px;height:386px;background:linear-gradient(90deg,rgba(63,150,104,0) 0%,#6fa7b9 35%,#4d7fb6 70%,#3e6aa0 100%)}
.hero-title{left:245px;top:192px;color:var(--white);font-size:30px;font-weight:600;line-height:1.3}
.hero-text{left:245px;top:285px;width:350px;color:var(--white);font-size:11px}

/* highlight panels */
.panel{top:478px;height:114px;color:var(--white)}
.panel-left{left:0;width:600px;background:var(--teal-dark)}
.panel-right{left:600px;width:600px;background:var(--green)}
.panel h3{color:var(--white);font-size:12px;font-weight:600;position:absolute;top:22px}
.panel p{position:absolute;top:42px;width:420px;font-size:9.5px;line-height:1.65}
.panel .more{position:absolute;top:80px;font-size:9px;font-weight:700}
.panel .divider{position:absolute;top:22px;left:150px;width:1px;height:70px;background:rgba(255,255,255,.25)}

/* welcome */
.welcome{top:592px;left:0;width:1200px;height:354px;background:var(--pale)}
.welcome-art{top:660px;left:197px;width:311px;height:208px;background:radial-gradient(ellipse at 50% 50%,#b9c7bd 0%,#dfe4e1 55%,#f2f3f3 100%)}
.welcome-title{left:610px;top:652px;font-size:21px;font-weight:600;line-height:1.3}
.welcome-copy{left:610px;top:718px;width:345px;font-size:10px;line-height:1.75}

/* sections */
.sec-title{width:1200px;left:0;text-align:center;font-size:21px;font-weight:600}
.sec-desc{left:310px;width:580px;text-align:center;font-size:10px;line-height:1.75}
.blob{top:965px;left:130px;width:800px;height:480px;border-radius:48% 52% 46% 54%;background:#f5f8fb}
.benefit{top:1076px;width:220px;display:flex;gap:14px}
.benefit .icon{width:50px;height:40px;flex:none;display:flex;align-items:center;justify-content:center}
.benefit h4{font-size:10.5px;font-weight:600;margin-bottom:6px}
.benefit p{font-size:9.5px;line-height:1.65}

.service{top:1340px;width:180px;text-align:center}
.service .pic{width:130px;height:130px;border-radius:50%;margin:0 auto 24px}
.service h4{font-size:12px;font-weight:600;line-height:1.4;margin-bottom:10px}
.service p{font-size:9.5px;line-height:1.65;width:140px;margin:0 auto}

/* before after */
.ba-pic{top:1803px;left:244px;width:346px;height:237px;background:linear-gradient(90deg,#e6dcd6 0%,#efe6e0 50%,#e9ded7 100%)}
.ba-handle{top:1908px;left:404px;width:26px;height:26px;border-radius:50%;background:var(--white);display:flex;align-items:center;justify-content:center}
.ba-title{left:610px;top:1822px;font-size:12px;font-weight:600}
.ba-copy{left:610px;top:1850px;width:345px;font-size:10px;line-height:1.75}

/* contact */
.contact{top:2078px;left:0;width:1200px;height:384px;background:linear-gradient(160deg,#eef0f1 0%,#e3e8ea 50%,#eceff0 100%)}
.contact-title{top:2082px;left:0;width:1200px;text-align:center;font-family:"Open Sans",sans-serif;font-size:28px;font-weight:600;color:#111;line-height:1.4}
.contact-lines{top:2126px;left:0;width:1200px;text-align:center;font-size:13.5px;color:#222;line-height:1.4}
.contact-lines b{font-weight:700}
.field{position:absolute;height:28px;width:176px;background:var(--white);font-size:13px;color:#777;padding:5px 9px}
.field.msg{width:367px;height:80px}
.send{top:2422px;left:496px;width:160px;height:30px;background:var(--green-btn);color:var(--white);border-radius:3px;font-size:13px;display:flex;align-items:center;justify-content:center}

/* footer */
.footer{top:2462px;left:0;width:1200px;height:311px;background:linear-gradient(120deg,var(--teal-dark) 0%,#0f6270 60%,#0b5361 100%);color:var(--white)}
.footer h4{position:absolute;top:48px;color:var(--white);font-size:12px;font-weight:600}
.footer ul{position:absolute;top:80px;list-style:none;font-size:10px;line-height:2.4}
.footer li::before{content:"›";margin-right:6px}
.footer-about{position:absolute;left:244px;top:86px;width:170px;font-size:9.5px;line-height:1.7}
.footer-brand{position:absolute;left:244px;top:38px;display:flex;align-items:center;gap:8px}
.footer-brand .brand-dot{background:var(--green);width:26px;height:26px}
.footer-brand .brand-name{color:var(--white);font-size:19px}
.footer-office{position:absolute;left:792px;top:86px;font-size:9.5px;line-height:1.7}
.footer-rule{position:absolute;left:244px;top:270px;width:712px;height:1px;background:rgba(255,255,255,.2)}
.footer-bottom{position:absolute;top:282px;font-size:9px}
</style>
</head>
<body>

<header class="abs topbar">
  <div class="abs brand"><span class="brand-dot"></span><span class="brand-name">TORVANE</span></div>
  <div class="abs help">Emergency Help<strong>555-014-2290</strong></div>
  <div class="abs vline" style="left:610px"></div>
  <div class="abs info" style="left:624px">
    <span class="ico"><svg width="9" height="11" viewBox="0 0 9 11"><path d="M4.5 0A4 4 0 0 0 .5 4c0 3 4 7 4 7s4-4 4-7a4 4 0 0 0-4-4zm0 5.5a1.5 1.5 0 1 1 0-3 1.5 1.5 0 0 1 0 3z" fill="#fff"/></svg></span>
    <span>PO Box 4410 Harlow Lane West<br>Avalon 9021</span>
  </div>
  <div class="abs vline" style="left:792px"></div>
  <div class="abs info" style="left:806px">
    <span class="ico"><svg width="11" height="11" viewBox="0 0 11 11"><circle cx="5.5" cy="5.5" r="4.5" fill="none" stroke="#fff" stroke-width="1.3"/><path d="M5.5 3v2.7l1.8 1.2" stroke="#fff" stroke-width="1.2" fill="none"/></svg></span>
    <span>Monday - Saturday - 8:00 - 18:00<br>Sunday - 8:00 - 14:00</span>
  </div>
</header>

<nav class="abs nav">
  <ul>
    <li class="active">Home</li><li>About ⌄</li><li>Services ⌄</li><li>Science ⌄</li><li>Testimonials ⌄</li><li>Contact us ⌄</li><li>Book an appointment</li>
  </ul>
  <div class="abs nav-tools">
    <svg width="14" height="13" viewBox="0 0 14 13"><path d="M1 1h2l2 7h7l1.5-5H4" fill="none" stroke="#fff" stroke-width="1.4"/><circle cx="6" cy="11" r="1.2" fill="#fff"/><circle cx="11" cy="11" r="1.2" fill="#fff"/></svg>
    <svg width="13" height="13" viewBox="0 0 13 13"><circle cx="5.5" cy="5.5" r="4" fill="none" stroke="#fff" stroke-width="1.6"/><path d="M8.5 8.5 12 12" stroke="#fff" stroke-width="1.8"/></svg>
  </div>
</nav>

<section>
  <div class="abs hero" role="img" aria-label="Soft green textured background"></div>
  <div class="abs hero-photo" role="img" aria-label="Photo of a clinician in blue scrubs holding a stethoscope"></div>
  <h1 class="abs hero-title">Restorative Medicine<br>To renew the world</h1>
  <p class="abs hero-text">Lorem ipsum dolor sit amet consectetur adipiscing elit sed do eiusmod tempor incididunt ut labore et dolore magna.</p>
  <div class="btn" style="left:248px;top:338px;width:142px;height:32px;border:1px solid rgba(255,255,255,.35);background:#1c6b5c;color:#fff">Make an appointment</div>
</section>

<section>
  <div class="abs panel panel-left">
    <svg class="abs" style="left:92px;top:30px" width="28" height="44" viewBox="0 0 28 44"><path d="M14 4c-5 0-7 5-5 10l-7 24 5 2 7-18 7 18 5-2-7-24c2-5 0-10-5-10z" fill="none" stroke="#fff" stroke-width="2.2"/></svg>
    <span class="divider"></span>
    <h3 style="left:169px">Patients</h3>
    <p style="left:169px">Lorem ipsum dolor sit amet consectetur adipiscing elit sed do Lorem ipsum dolor sit amet consectetur adipiscing</p>
    <span class="more" style="left:169px">Read more</span>
  </div>
  <div class="abs panel panel-right">
    <svg class="abs" style="left:38px;top:30px" width="32" height="44" viewBox="0 0 32 44"><path d="M4 2v12a9 9 0 0 0 18 0V2M13 23v8a8 8 0 0 0 16 0v-6" fill="none" stroke="#fff" stroke-width="2.2"/><circle cx="29" cy="22" r="3" fill="none" stroke="#fff" stroke-width="2"/></svg>
    <span class="divider" style="left:100px"></span>
    <h3 style="left:116px">Professionals</h3>
    <p style="left:116px">Lorem ipsum dolor sit amet consectetur adipiscing elit sed do Lorem ipsum dolor sit amet consectetur adipiscing</p>
    <span class="more" style="left:116px">Read more</span>
  </div>
</section>

<section>
  <div class="abs welcome"></div>
  <div class="abs welcome-art" role="img" aria-label="Illustration of a human figure made of scattered particles"></div>
  <h2 class="abs welcome-title">Welcome to Torvane Center<br>For Restorative medicine</h2>
  <div class="abs welcome-copy">
    <p>Lorem ipsum dolor sit amet consectetur adipiscing elit sed do Lorem ipsum dolor sit amet consectetur adipiscing elit sed do Lorem ipsum dolor sit amet consectetur adipiscing elit sed do Lorem ipsum dolor sit amet consectetur adipiscing elit sed do Lorem ipsum dolor sit amet consectetur adipiscing elit sed do</p>
    <p style="margin-top:8px">Lorem ipsum dolor sit amet consectetur adipiscing elit sed do eiusmod tempor incididunt ut labore et dolore magna aliqua.</p>
  </div>
  <div class="btn btn-solid" style="left:610px;top:858px;width:118px;height:30px">Discover more</div>
</section>

<section>
  <div class="abs blob"></div>
  <h2 class="abs sec-title" style="top:972px">Patients Benefits</h2>
  <p class="abs sec-desc" style="top:1012px">Lorem ipsum dolor sit amet consectetur adipiscing elit sed do Lorem ipsum dolor sit amet consectetur adipiscing elit sed do Lorem ipsum dolor sit amet consectetur adipiscing</p>

  <div class="abs benefit" style="left:255px">
    <div class="icon"><svg width="36" height="36" viewBox="0 0 36 36"><circle cx="18" cy="18" r="17" fill="#eaf1f5"/><circle cx="18" cy="12" r="5" fill="#0d5b69"/><path d="M8 30c0-6 4-10 10-10s10 4 10 10z" fill="#0d5b69"/><path d="M17 22h2v6h-2z" fill="#fff"/></svg></div>
    <div><h4>Qualified Doctors</h4><p>Lorem ipsum dolor sit amet consectetur adipiscing elit sed do eiusmod.</p></div>
  </div>
  <div class="abs benefit" style="left:500px">
    <div class="icon"><svg width="36" height="36" viewBox="0 0 36 36"><circle cx="18" cy="18" r="17" fill="#eaf1f5"/><circle cx="18" cy="11" r="4" fill="#0d5b69"/><circle cx="10" cy="14" r="3" fill="#0d5b69"/><circle cx="26" cy="14" r="3" fill="#0d5b69"/><path d="M11 28c0-5 3-9 7-9s7 4 7 9zM4 27c0-4 2-7 6-7 2 0 3 1 3 1l-3 6zM32 27c0-4-2-7-6-7-2 0-3 1-3 1l3 6z" fill="#0d5b69"/></svg></div>
    <div><h4>Medical Counselling</h4><p>Lorem ipsum dolor sit amet consectetur adipiscing elit sed do eiusmod.</p></div>
  </div>
  <div class="abs benefit" style="left:745px">
    <div class="icon"><svg width="36" height="36" viewBox="0 0 36 36"><circle cx="18" cy="18" r="17" fill="#eaf1f5"/><circle cx="18" cy="18" r="11" fill="#fff" stroke="#0d5b69" stroke-width="2"/><path d="M18 11v7l5 3" stroke="#0d5b69" stroke-width="2" fill="none"/></svg></div>
    <div><h4>24 Hours Service</h4><p>Lorem ipsum dolor sit amet consectetur adipiscing elit sed do eiusmod.</p></div>
  </div>

  <h2 class="abs sec-title" style="top:1225px">Our services</h2>
  <p class="abs sec-desc" style="top:1265px">Lorem ipsum dolor sit amet consectetur adipiscing elit sed do Lorem ipsum dolor sit amet consectetur adipiscing elit sed do Lorem ipsum dolor sit amet consectetur adipiscing</p>

  <div class="abs service" style="left:235px">
    <div class="pic" role="img" aria-label="Photo of hands giving a gentle treatment" style="background:radial-gradient(circle,#f2ded6 0%,#e4cbc1 100%)"></div>
    <h4>needle-less<br>regenerative injection<br>therapy</h4>
    <p>Lorem ipsum dolor sit amet consectetur adipiscing elit sed do eiusmod tempor.</p>
  </div>
  <div class="abs service" style="left:418px">
    <div class="pic" role="img" aria-label="Photo of a body contour treatment" style="background:radial-gradient(circle,#efe3d8 0%,#dccab9 100%)"></div>
    <h4>Stem cell treatments</h4>
    <p>Lorem ipsum dolor sit amet consectetur adipiscing elit sed do eiusmod tempor.</p>
  </div>
  <div class="abs service" style="left:600px">
    <div class="pic" role="img" aria-label="Photo of a patient receiving a skin treatment" style="background:radial-gradient(circle,#eddcd2 0%,#a9c9dd 100%)"></div>
    <h4>Bioidentical hormone<br>therapy</h4>
    <p>Lorem ipsum dolor sit amet consectetur adipiscing elit sed do eiusmod tempor.</p>
  </div>
  <div class="abs service" style="left:784px">
    <div class="pic" role="img" aria-label="Photo of a patient in a treatment room" style="background:radial-gradient(circle,#d9e6ea 0%,#9fc3cf 100%)"></div>
    <h4>Treatment for chronic<br>illness</h4>
    <p>Lorem ipsum dolor sit amet consectetur adipiscing elit sed do eiusmod tempor.</p>
  </div>
  <div class="btn btn-line" style="left:283px;top:1608px;width:84px;height:26px">Read more</div>
  <div class="btn btn-line" style="left:466px;top:1576px;width:84px;height:26px">Read more</div>
  <div class="btn btn-line" style="left:648px;top:1592px;width:84px;height:26px">Read more</div>
  <div class="btn btn-line" style="left:832px;top:1592px;width:84px;height:26px">Read more</div>
</section>

<section>
  <h2 class="abs sec-title" style="top:1695px">Before and After Result</h2>
  <p class="abs sec-desc" style="top:1735px">Lorem ipsum dolor sit amet consectetur adipiscing elit sed do Lorem ipsum dolor sit amet consectetur adipiscing elit sed do Lorem ipsum dolor sit amet consectetur</p>
  <div class="abs ba-pic" role="img" aria-label="Before and after comparison photo of facial skin"></div>
  <div class="abs" style="left:416px;top:1803px;width:2px;height:237px;background:#fff"></div>
  <div class="abs ba-handle"><svg width="14" height="8" viewBox="0 0 14 8"><path d="M5 0 0 4l5 4zM9 0l5 4-5 4z" fill="#333"/></svg></div>
  <h3 class="abs ba-title">Watch the video</h3>
  <div class="abs ba-copy">
    <p>Lorem ipsum dolor sit amet consectetur adipiscing elit sed do Lorem ipsum dolor sit amet consectetur adipiscing elit sed do Lorem ipsum dolor sit amet consectetur Lorem ipsum dolor sit amet consectetur adipiscing elit sed do Lorem ipsum dolor sit amet consectetur adipiscing elit sed do Lorem ipsum dolor sit amet consectetur</p>
    <p style="margin-top:8px">Lorem ipsum dolor sit amet consectetur adipiscing elit sed do eiusmod tempor incididunt ut labore et dolore magna aliqua.</p>
  </div>
  <div class="btn btn-solid" style="left:610px;top:1992px;width:100px;height:30px">Watch now</div>
</section>

<section>
  <div class="abs contact" role="img" aria-label="Faded map background"></div>
  <h2 class="abs contact-title">Contact us</h2>
  <div class="abs contact-lines">
    <p><b>Address:</b> 48 Cedar Row, Westbrook, United States</p>
    <p><b>Phone:</b> (555)014-2290</p>
    <p><b>Email:</b> hello@torvane.example</p>
  </div>
  <div class="field" style="left:400px;top:2192px">First name :</div>
  <div class="field" style="left:591px;top:2192px">Last name :</div>
  <div class="field" style="left:400px;top:2238px">Your email :</div>
  <div class="field" style="left:591px;top:2238px">Your phone :</div>
  <div class="field" style="left:400px;top:2284px">Your company :</div>
  <div class="field" style="left:591px;top:2284px">Subject :</div>
  <div class="field msg" style="left:400px;top:2330px">Your message :</div>
  <div class="abs send">Send message</div>
</section>

<footer class="abs footer">
  <div class="footer-brand"><span class="brand-dot"></span><span class="brand-name">TORVANE</span></div>
  <p class="footer-about">Lorem ipsum dolor sit amet consectetur adipiscing elit sed do Lorem ipsum dolor sit amet consectetur adipiscing elit sed do Lorem ipsum dolor sit amet consectetur</p>

  <h4 style="left:427px">Departments</h4>
  <ul style="left:427px">
    <li>Regenerative injection</li><li>Stem cell treatments</li><li>Bioidentical hormone therapy</li><li>Treatment for chronic illness</li><li>Neurodegenerative diseases</li><li>Skin rejuvenation</li>
  </ul>

  <h4 style="left:610px">Quick Links</h4>
  <ul style="left:610px">
    <li>About Us</li><li>Departments</li><li>Find a Doctor</li><li>FAQ</li><li>Timetable</li><li>News</li>
  </ul>

  <h4 style="left:792px">Head Office</h4>
  <div class="footer-office">
    <p>PO Box 4410 Harlow Lane West<br>Avalon 9021</p>
    <p style="margin-top:14px">Mon-Thu: 9:30 – 21:00<br>Fri: 6:00 – 21:00<br>Sat: 10:00 – 15:00</p>
  </div>

  <div class="footer-rule"></div>
  <p class="footer-bottom" style="left:244px">Torvane Center for Restorative Medicine © All Rights Reserved</p>
  <p class="footer-bottom" style="left:794px">Terms &amp; Conditions</p>
  <p class="footer-bottom" style="left:896px">Privacy Policy</p>
</footer>

</body>
</html>
```